Bright Ledger Hosting Workdeck 720 Flyer

We have a requirement to start sending out product / service information to our clients and resellers. Currently this type of communication is only via the LinkedIn/ Twitter / Blog articles and we want to change this to an email campaign with pdf and the ability to print and send by post.

We have a powerpoint draft of the flyer that will be a pdf and potentially a handout but it looks like a powerpoint and not something classy. I have included the powerpoint and four images along with our current logo (although this may change soon)

Target Market(s)

MSP Resellers, Direct Clients

Industry/Entity Type

It Service

Colors

Designer to choose colors to be used in the design.

Requirements
Must have
• The flow and feel from our website and social media so that it has our identity. Our core colors are on the website. Anything new must be complementary.
• Modern and technical feel
Nice to have
• Sense of security and trust. Our new strap line is to be "Simple, Safe, Secure" so some experimentation on this would be nice
Should not have
• nothing of note

```html
<!DOCTYPE html>
<html lang="en">
<head>
<meta charset="utf-8">
<title>Know the Facts – Bright Ledger Hosting</title>
<link rel="stylesheet" href="https://fonts.googleapis.com/css2?family=Montserrat:wght@300;400;600;700;800&display=swap">
<style>
  :root {
    --stage: #c9c9c9;
    --slate-dark: #45484d;
    --slate-mid: #5d6066;
    --slate-light: #83868b;
    --green: #3d9a3f;
    --green-light: #6db768;
    --paper-text: #eef0f1;
    --photo-wall: #d7dccb;
    --photo-wall-dark: #aab3a4;
    --photo-desk: #3a4148;
    --strip-sea: #7f9aa3;
  }
  * { box-sizing: border-box; margin: 0; padding: 0; }
  html, body {
    width: 1200px; height: 833px; overflow: hidden;
    background: var(--stage);
    font-family: "Montserrat", sans-serif;
  }
  .spread {
    position: absolute; left: 50px; top: 28px;
    width: 1100px; height: 778px;
    display: flex;
    box-shadow: 0 10px 30px rgba(0,0,0,0.25);
  }
  .page { position: relative; width: 550px; height: 778px; overflow: hidden; }
  .page--text {
    background: linear-gradient(100deg, var(--slate-dark) 0%, var(--slate-mid) 55%, var(--slate-light) 100%);
  }
  .page--photo {
    background:
      linear-gradient(180deg, transparent 72%, var(--photo-desk) 72%, #252a30 100%),
      radial-gradient(ellipse at 70% 40%, var(--photo-wall) 0%, var(--photo-wall-dark) 100%);
  }
  .header-band { position: absolute; left: 0; top: 0; width: 720px; height: 130px; z-index: 1; }
  .headline {
    position: absolute; left: 62px; top: 38px; z-index: 2;
    font-size: 54px; font-weight: 800; letter-spacing: 1px;
    color: #ffffff; white-space: nowrap;
    text-shadow: 0 3px 6px rgba(0,0,0,0.3);
  }
  .copy {
    position: absolute; left: 70px; top: 150px; width: 415px;
    color: var(--paper-text);
    font-size: 12.5px; font-weight: 400; line-height: 1.5;
    text-align: justify;
  }
  .copy p { margin-bottom: 14px; }
  .copy p.lead { margin-bottom: 18px; }
  .subhead {
    display: inline-block;
    background: var(--green);
    color: #ffffff;
    font-weight: 700; font-size: 15px;
    padding: 4px 40px 4px 46px;
    margin: 0 0 18px -70px;
  }
  .photo-strip {
    position: absolute; left: 0; bottom: 0; width: 550px; height: 150px;
    background: linear-gradient(180deg, #5a6066 0%, var(--strip-sea) 30%, #5c7079 65%, #2e353b 100%);
  }
  .photo-strip::before {
    content: ""; position: absolute; left: 0; top: -30px; width: 100%; height: 40px;
    background: linear-gradient(180deg, transparent, #5a6066);
  }
</style>
</head>
<body>
  <main class="spread">
    <section class="page page--text">
      <p class="copy">
      </p>
      <div class="copy">
        <p class="lead">Corvane Workdeck 720 is quickly becoming the "go to" for businesses and the adoption of this shows no signs of slowing down anytime soon. There is no doubting that the services that they provide are robust and the uptime statistics certainly demonstrate that they are focused on providing a solid infrastructure for their services.</p>
        <h2 class="subhead">So, nothing to worry about then ?</h2>
        <p>Wrong, unfortunately, there is a common misconception that this service also provides backups of your data. In fact the responsibility of this remains with you.</p>
        <p>The reality is that without backups, you are left open to data loss and reports state that 1 in 3 businesses that have adopted cloud technology have experienced this. Without a change in the mindset, you are increasing risk and could lead to damaging repercussions for your business.</p>
        <p>You need to take control of your data and introduce a cloud backup solution that takes care of the day to day backups of your Workdeck 720, provides you with data protection and a retention policy that suits your business requirements</p>
      </div>
      <div class="photo-strip" role="img" aria-label="Continuation of the desk photograph: dark tabletop edge with a soft blue-grey background"></div>
    </section>
    <section class="page page--photo" role="img" aria-label="Photograph: young inventor in a dark suit wearing goggles and a home-made wired helmet, writing at a desk beside a vintage meter"></section>

    <svg class="header-band" viewBox="0 0 720 130" aria-hidden="true">
      <defs>
        <linearGradient id="bandFill" x1="0" x2="1" y1="0" y2="0">
          <stop offset="0" stop-color="#2f8a35"/>
          <stop offset="0.75" stop-color="#4ea84d"/>
          <stop offset="1" stop-color="#7cc076"/>
        </linearGradient>
      </defs>
      <path d="M0 0 H720 V62 Q600 118 470 122 Q240 118 0 92 Z" fill="url(#bandFill)"/>
    </svg>
    <h1 class="headline">KNOW THE FACTS</h1>
  </main>
</body>
</html>
```